interior designer/stylist looking for a letter press business card to reflect the stylish work

Hello Designers,
I need a business card design for an company called Halvard Interior Design. I'm aiming at the high end residential and private client market in London providing sleek simple interiors. I'd like my business card to be tackboard worthy and expensive looking, i want people to pin it and for it to have a sought after look, and want prospective customers to hire me as their interior designer as my card is so beautiful.
I love letter press design. I also like the use of colour/foil on the edge.
Colour combos & general things I like -
Black and White
Navy Blue and Gold
Neutral colours (muted palette of greys whites navys beiges)
White Marble & brass
Morvane (fashion designer)
....also open to other suggestions....
Please dont take the pink in the attached photos too literally. i'd like the card to look more masculine than feminine.
I'd like Halvard on one side in one font, with interior design underneath so one word will make the statement....... unless anyone has any other ideas, open to suggestions.
I'd like a really simple font and for the whole card to look very graphic.
my details -
Petra Quillby
Interior Designer & Stylist
email petra@halvardinteriordesign.co.uk
phone +447813554019
website wwww.halvardinteriordesign.co.uk
GO GO GO!! EXCITED TO SEE THE OUTCOME!!
x L
Target Market(s)
High End Residential and private clients
Industry/Entity Type
Business
Contact Information for Business Card
Halvard Interior Design & Styling
Petra Quillby
phone +447813554019

```html
<!DOCTYPE html>
<html lang="en">
<head>
<meta charset="utf-8">
<title>Halvard Interior Design &amp; Styling — Business Card</title>
<link rel="stylesheet" href="https://fonts.googleapis.com/css2?family=Open+Sans:wght@300;400;700&display=swap">
<style>
  :root {
    --backdrop: #5f5f5f;
    --card-stock: #f4f3ef;
    --foil-gold: #b8860f;
    --card-shadow: rgba(0, 0, 0, 0.35);
  }

  * { box-sizing: border-box; margin: 0; padding: 0; }

  html, body {
    width: 870px;
    height: 1200px;
    overflow: hidden;
    background: var(--backdrop);
  }

  .sheet {
    width: 870px;
    height: 1200px;
    display: flex;
    flex-direction: column;
    align-items: center;
    justify-content: space-around;
    padding: 60px 0;
  }

  .card {
    position: relative;
    width: 560px;
    height: 320px;
    background: var(--card-stock);
    box-shadow: 0 14px 30px var(--card-shadow);
    font-family: "Open Sans", Arial, sans-serif;
    color: var(--foil-gold);
  }

  /* Front: contact details */
  .card-front__details {
    position: absolute;
    top: 62px;
    left: 200px;
    width: 300px;
    text-align: center;
    line-height: 1.35;
  }

  .card-front__name {
    font-weight: 700;
    font-size: 17px;
    letter-spacing: 0.2px;
  }

  .card-front__role {
    font-weight: 400;
    font-size: 14px;
    margin-bottom: 4px;
  }

  .card-front__contact {
    font-weight: 400;
    font-size: 12.5px;
    list-style: none;
  }

  .card-front__rules {
    position: absolute;
    left: 0;
    bottom: 58px;
    width: 540px;
    height: 12px;
  }

  /* Back: wordmark */
  .card-back__wordmark {
    position: absolute;
    inset: 0;
    display: flex;
    align-items: center;
    justify-content: center;
    font-weight: 300;
    font-size: 62px;
    letter-spacing: 6px;
    text-transform: uppercase;
  }
</style>
</head>
<body>
  <main class="sheet">
    <section class="card card-front" aria-label="Business card front">
      <div class="card-front__details">
        <p class="card-front__name">Petra Quillby</p>
        <p class="card-front__role">Interior Designer &amp; Stylist</p>
        <ul class="card-front__contact">
          <li>+447813554019</li>
          <li>petra@halvardinteriordesign.co.uk</li>
          <li>www.halvardinteriordesign.co.uk</li>
        </ul>
      </div>
      <svg class="card-front__rules" viewBox="0 0 540 12" aria-hidden="true">
        <line x1="0" y1="2" x2="540" y2="2" stroke="var(--foil-gold)" stroke-width="2"/>
        <line x1="0" y1="9" x2="540" y2="9" stroke="var(--foil-gold)" stroke-width="2"/>
      </svg>
    </section>

    <section class="card card-back" aria-label="Business card back">
      <p class="card-back__wordmark">Halvard</p>
    </section>
  </main>
</body>
</html>
```